We are a all around maintence company for outdoor services. Commercial and residential: mowing, sprinkler repairs, power washing, parking lot striping, tree trimming, gutters cleaning, pond cleaning,feeding and fertilizing, flower bed clean up and fence repair.

Industry/Entity Type

It Company

Contact Information for Business Card

Harbrook Yard Services
R.L. Vandermolt
Cell 555-312-4870
P.O. Box 4518
Brindlewood,Vr 80257
Office 555-629-3051
Fax 555-629-3057

```html
<!DOCTYPE html>
<html lang="en">
<head>
<meta charset="utf-8">
<title>Harbrook Yard Services – Business Card</title>
<link href="https://fonts.googleapis.com/css2?family=Gilda+Display&family=Questrial&display=swap" rel="stylesheet">
<style>
  :root {
    --page-bg: #e9e6e1;
    --card-light: #ffffff;
    --card-dark: #3c3e3e;
    --ink-grey: #6d6f70;
    --ink-soft: #8b8d8e;
    --ink-white: #f2f2f2;
    --accent-green: #6cc04a;
    --accent-teal: #5bc2d6;
    --mark-grey: #b9bbbc;
  }
  * { margin: 0; padding: 0; box-sizing: border-box; }
  html, body {
    width: 734px; height: 1200px; overflow: hidden;
    background: var(--page-bg);
  }
  .canvas { position: relative; width: 734px; height: 1200px; }
  .card {
    position: absolute; left: 87px; width: 560px; height: 320px;
    border-radius: 4px;
    box-shadow: 0 6px 18px rgba(0,0,0,0.18);
    overflow: hidden;
  }
  .card--front { top: 110px; background: var(--card-light); }
  .card--back  { top: 770px; background: var(--card-dark); }

  .brand-square {
    position: absolute; width: 62px; height: 62px;
    background: var(--mark-grey);
  }
  .company-name {
    position: absolute;
    font-family: "Gilda Display", serif;
    font-weight: 400; letter-spacing: 0.5px;
    white-space: nowrap;
  }

  /* front */
  .card--front .brand-square { left: 62px; top: 78px; }
  .card--front .company-name {
    left: 146px; top: 86px; font-size: 29px; color: var(--ink-soft);
  }
  .holder-name {
    position: absolute; left: 146px; top: 150px;
    font-family: "Questrial", sans-serif; font-size: 25px;
    color: var(--ink-grey);
  }
  .contact-list {
    position: absolute; left: 62px; top: 222px;
    font-family: "Questrial", sans-serif; font-size: 14px;
    color: var(--ink-grey);
  }
  .contact-row { display: flex; gap: 22px; margin-bottom: 10px; }
  .contact-item { display: flex; align-items: center; gap: 6px; white-space: nowrap; }
  .contact-item svg { width: 14px; height: 14px; fill: var(--accent-green); flex: none; }

  /* back */
  .service-heading {
    position: absolute; left: 40px; top: 16px;
    font-family: "Questrial", sans-serif; font-size: 15px;
    color: var(--accent-green);
  }
  .service-list {
    position: absolute; left: 40px; top: 44px;
    font-family: "Questrial", sans-serif; list-style: none;
  }
  .service-list li {
    display: flex; align-items: center; gap: 9px;
    font-size: 14px; line-height: 25px; color: var(--ink-white);
  }
  .service-list li svg { width: 13px; height: 13px; flex: none; }
  .service-list .tick-box { fill: none; stroke: var(--accent-teal); stroke-width: 1.4; }
  .service-list .tick { fill: none; stroke: var(--accent-teal); stroke-width: 2; stroke-linecap: round; stroke-linejoin: round; }
  .card--back .brand-square { left: 366px; top: 62px; width: 92px; height: 92px; }
  .card--back .company-name {
    right: 34px; top: 190px; font-size: 25px; color: var(--ink-white);
  }
</style>
</head>
<body>
<main class="canvas">

  <section class="card card--front" aria-label="Business card front">
    <div class="brand-square" aria-hidden="true"></div>
    <h1 class="company-name">Harbrook Yard Services</h1>
    <p class="holder-name">R.L. Vandermolt</p>
    <div class="contact-list">
      <div class="contact-row">
        <span class="contact-item">
          <svg viewBox="0 0 14 14" aria-label="Cell"><rect x="3.5" y="0.5" width="7" height="13" rx="1.5"/><rect x="5" y="2.5" width="4" height="8" fill="#fff"/></svg>
          555-312-4870
        </span>
        <span class="contact-item">
          <svg viewBox="0 0 14 14" aria-label="Office"><path d="M1 4c0-1.5 2.5-3 6-3s6 1.5 6 3v1.5H10V4H4v1.5H1z"/><rect x="2" y="7" width="10" height="6" rx="1"/></svg>
          555-629-3051
        </span>
        <span class="contact-item">
          <svg viewBox="0 0 14 14" aria-label="Fax"><rect x="4" y="0.5" width="6" height="4"/><rect x="1" y="5" width="12" height="7" rx="1"/><rect x="4" y="9" width="6" height="4.5" fill="#fff" stroke="#6cc04a"/></svg>
          555-629-3057
        </span>
      </div>
      <div class="contact-row">
        <span class="contact-item">
          <svg viewBox="0 0 14 14" aria-label="Address"><path d="M7 0.5a4.5 4.5 0 0 0-4.5 4.5C2.5 8.5 7 13.5 7 13.5S11.5 8.5 11.5 5A4.5 4.5 0 0 0 7 0.5z"/><circle cx="7" cy="5" r="1.7" fill="#fff"/></svg>
          P.O. Box 4518, Brindlewood,Vr 80257
        </span>
      </div>
    </div>
  </section>

  <section class="card card--back" aria-label="Business card back">
    <p class="service-heading">Commercial and residential</p>
    <ul class="service-list">
      <li><svg viewBox="0 0 13 13"><rect class="tick-box" x="0.7" y="0.7" width="11.6" height="11.6"/><path class="tick" d="M3 6.5l2.5 2.5L10 3.5"/></svg>Mowing</li>
      <li><svg viewBox="0 0 13 13"><rect class="tick-box" x="0.7" y="0.7" width="11.6" height="11.6"/><path class="tick" d="M3 6.5l2.5 2.5L10 3.5"/></svg>Sprinkler repairs</li>
      <li><svg viewBox="0 0 13 13"><rect class="tick-box" x="0.7" y="0.7" width="11.6" height="11.6"/><path class="tick" d="M3 6.5l2.5 2.5L10 3.5"/></svg>Power washing</li>
      <li><svg viewBox="0 0 13 13"><rect class="tick-box" x="0.7" y="0.7" width="11.6" height="11.6"/><path class="tick" d="M3 6.5l2.5 2.5L10 3.5"/></svg>Parking lot striping</li>
      <li><svg viewBox="0 0 13 13"><rect class="tick-box" x="0.7" y="0.7" width="11.6" height="11.6"/><path class="tick" d="M3 6.5l2.5 2.5L10 3.5"/></svg>Tree trimming</li>
      <li><svg viewBox="0 0 13 13"><rect class="tick-box" x="0.7" y="0.7" width="11.6" height="11.6"/><path class="tick" d="M3 6.5l2.5 2.5L10 3.5"/></svg>Gutters cleaning</li>
      <li><svg viewBox="0 0 13 13"><rect class="tick-box" x="0.7" y="0.7" width="11.6" height="11.6"/><path class="tick" d="M3 6.5l2.5 2.5L10 3.5"/></svg>Pond cleaning</li>
      <li><svg viewBox="0 0 13 13"><rect class="tick-box" x="0.7" y="0.7" width="11.6" height="11.6"/><path class="tick" d="M3 6.5l2.5 2.5L10 3.5"/></svg>Feeding and fertilizing</li>
      <li><svg viewBox="0 0 13 13"><rect class="tick-box" x="0.7" y="0.7" width="11.6" height="11.6"/><path class="tick" d="M3 6.5l2.5 2.5L10 3.5"/></svg>Flower bed clean up</li>
      <li><svg viewBox="0 0 13 13"><rect class="tick-box" x="0.7" y="0.7" width="11.6" height="11.6"/><path class="tick" d="M3 6.5l2.5 2.5L10 3.5"/></svg>Fence repair</li>
    </ul>
    <div class="brand-square" aria-hidden="true"></div>
    <p class="company-name">Harbrook Yard Services</p>
  </section>

</main>
</body>
</html>
```